New business card design needed for Trucking/Staffing company!

I am looking for a business card design. The business name is Harbor Lane Freightworks, LLC. This company is a staffing company for commercial drivers/truck drivers. Most of our customers are trucking/supply companies. Our colors are blue/black/white/grey. The info I have on my current business cards is
-Spot for a name
-2 lines for an address
-3 lines for Office, cell, and fax
-email
-website(currently on backside of card with logo but can go anywhere)
Updates

Project Deadline Extended
Reason: Open to more designs

Target Market(s)

Trucking companies, building supply companies

Industry/Entity Type

Business

Contact Information for Business Card

Edgy but professional

Font styles to use
Other font styles liked:
• Open to suggestions

Colors
0555a3
000000
ffffff
9d9d9d

Requirements
Must have
• Must have the logo incorporated

```html
<!DOCTYPE html>
<html lang="en">
<head>
<meta charset="utf-8">
<title>Harbor Lane Freightworks — Business Cards</title>
<link href="https://fonts.googleapis.com/css2?family=Saira:wght@700&family=Open+Sans:wght@400;600&family=Tinos&display=swap" rel="stylesheet">
<style>
  :root {
    --blue: #0555a3;
    --brand-blue: #1f35a8;
    --black: #000000;
    --white: #ffffff;
    --grey: #9d9d9d;
    --grey-light: #c9c9cb;
    --stage: #e6e7ea;
    --ink: #1a1a1a;
  }
  * { box-sizing: border-box; margin: 0; padding: 0; }
  html, body { width: 1200px; height: 800px; overflow: hidden; }
  body {
    background: var(--stage);
    font-family: "Open Sans", sans-serif;
    position: relative;
  }
  .card {
    position: absolute;
    top: 250px;
    width: 525px;
    height: 300px;
    overflow: hidden;
    box-shadow: 0 6px 18px rgba(0,0,0,0.18);
  }
  .card--front { left: 50px; background: var(--black); }
  .card--back { left: 625px; background: var(--grey-light); }

  .texture {
    position: absolute;
    inset: 0;
  }
  .texture--dark {
    background: radial-gradient(ellipse at 70% 60%, #3a3a3a 0%, #121212 45%, #000 80%);
  }
  .texture--light {
    top: 78px;
    background: linear-gradient(160deg, #b8b8ba 0%, #d3d3d5 40%, #a9a9ac 75%, #bdbdc0 100%);
  }

  .front-band {
    position: absolute;
    left: 0; right: 0;
    top: 70px;
    height: 140px;
    background: var(--white);
  }

  .brand {
    position: absolute;
    display: flex;
    align-items: center;
    gap: 12px;
    font-family: "Saira", sans-serif;
    font-weight: 700;
    color: var(--brand-blue);
    text-transform: uppercase;
    line-height: 1.05;
  }
  .brand__mark {
    flex: none;
    width: 22px; height: 22px;
    border-radius: 50%;
    background: var(--brand-blue);
  }
  .brand--front { left: 70px; top: 102px; font-size: 30px; }
  .brand--back { right: 26px; top: 100px; font-size: 22px; text-align: right; }

  .back-band {
    position: absolute;
    left: 0; right: 0; top: 0;
    height: 78px;
    background: var(--black);
  }
  .back-corner {
    position: absolute;
    right: 0; top: 78px;
    width: 190px; height: 90px;
    background: var(--black);
  }
  .brand--back { color: var(--brand-blue); background: var(--white); padding: 8px 12px; }

  .person {
    position: absolute;
    left: 28px; top: 92px;
  }
  .person__name {
    font-size: 30px;
    color: var(--brand-blue);
    font-weight: 400;
    line-height: 1;
  }
  .person__title {
    font-family: "Tinos", serif;
    font-size: 15px;
    color: var(--ink);
    margin-left: 96px;
  }

  .contacts {
    position: absolute;
    right: 28px; bottom: 22px;
    list-style: none;
    font-size: 12.5px;
    color: var(--ink);
    text-align: right;
  }
  .contacts li {
    display: flex;
    align-items: center;
    justify-content: flex-end;
    gap: 7px;
    line-height: 19px;
  }
  .contacts svg { width: 12px; height: 12px; fill: var(--brand-blue); flex: none; }
</style>
</head>
<body>

<section class="card card--front">
  <div class="texture texture--dark" role="img" aria-label="Dark photographic texture of truck tyres in motion"></div>
  <div class="front-band"></div>
  <div class="brand brand--front">
    <span class="brand__mark"></span>
    <span>Harbor Lane<br>Freightworks, LLC</span>
  </div>
</section>

<section class="card card--back">
  <div class="back-band"></div>
  <div class="texture texture--light" role="img" aria-label="Silver photographic texture of truck tyres in motion"></div>
  <div class="back-corner"></div>
  <div class="brand brand--back">
    <span>Harbor Lane<br>Freightworks, LLC</span>
  </div>

  <div class="person">
    <h1 class="person__name">Dana Whitfield</h1>
    <p class="person__title">Title</p>
  </div>

  <ul class="contacts">
    <li>0418-220-617
      <svg viewBox="0 0 12 12"><rect x="3" y="0.5" width="6" height="11" rx="1.2"/></svg></li>
    <li>5129-306-482
      <svg viewBox="0 0 12 12"><path d="M1 4c0-2 2-3 5-3s5 1 5 3l-2 1-1-2H4L3 5zM2 6h8l1 5H1z"/></svg></li>
    <li>dana@harborlanefw.com
      <svg viewBox="0 0 12 12"><path d="M0 2h12v8H0zM1 3l5 4 5-4v-.2H1z" fill-rule="evenodd"/></svg></li>
    <li>www.harborlanefw.com
      <svg viewBox="0 0 12 12"><circle cx="6" cy="6" r="5.5"/></svg></li>
    <li>Calloway Street 48 Brenton, NY
      <svg viewBox="0 0 12 12"><path d="M6 0a4 4 0 0 1 4 4c0 3-4 8-4 8S2 7 2 4a4 4 0 0 1 4-4zm0 2.5a1.5 1.5 0 1 0 0 3 1.5 1.5 0 0 0 0-3z" fill-rule="evenodd"/></svg></li>
  </ul>
</section>

</body>
</html>
```